Design an eBook cover for The Honest Chaos Of The Last Little One

The Honest Chaos Of the Last Little One was a blog post written in 2012 that has since gone viral, and read by millions. I am combining it with some other popular posts to make a short eBook designed to appeal to anyone who has three kids, is considering three kids or wants to justify their decision NEVER to have three kids.

Read the post here: http://nappydiaryhq.examplepress.com.au/2012/02/honest-chaos-last-little-one.html. You can also see the artwork on my blog to get an idea of what I might be looking for.

The book cover must be absolutely eye catching and unambiguous. The book is funny and heart felt, very real and a bit grubby. It can be simple but it must be funny and clever. I would prefer drawings/cartoons rather than photographic images. The cover must allow space for a "quote" from a well-known blogger.

I can't wait to see what you come up with. Thank you!

Target Market(s)

Parents, mothers to be, people with a sense of humour

Font styles to use
Sans Serif

Requirements
Must have
• Eye catching title "The Honest Chaos Of The Last Little One"
• Author name: Loretta Vanstrand
• Great image
• Space for a 'this is brilliant etc etc' quote from big-name blogger.
• Must be able to be uploaded to Pagewell as an eBook cover
Nice to have
• Pithy one liner explaining the book underneath the main title.
• Memorable picture/image - simple, eye catching.
• Nice to have options for spine and back cover.
• Please look at my blog for more ideas www.nappydiaryhq.examplepress.com
Should not have
• My picture.
• No stock images or photos.

```html
<!DOCTYPE html>
<html lang="en">
<head>
<meta charset="utf-8">
<title>The Honest Chaos Of The Last Little One — eBook Cover</title>
<link rel="stylesheet" href="https://fonts.googleapis.com/css2?family=Graduate&family=Montserrat:wght@500;600;700&family=Permanent+Marker&display=swap">
<style>
  :root {
    --ink: #000000;
    --paper: #ffffff;
    --ribbon: #ee1d52;
    --ribbon-deep: #a50d35;
    --branch-light: #9a9a9a;
    --branch-mid: #4a4a4a;
    --trunk: #d8d8d8;
  }
  * { margin: 0; padding: 0; box-sizing: border-box; }
  html, body { width: 776px; height: 1200px; overflow: hidden; background: var(--ink); }
  .cover {
    position: relative;
    width: 776px;
    height: 1200px;
    background: var(--ink);
    overflow: hidden;
    font-family: "Montserrat", sans-serif;
    color: var(--paper);
  }
  .kicker {
    position: absolute;
    top: 8px; left: 0; right: 0;
    text-align: center;
    font-weight: 700;
    font-size: 19px;
    letter-spacing: 11px;
    text-indent: 11px;
    white-space: nowrap;
  }
  .tree-art {
    position: absolute;
    inset: 0;
    width: 776px; height: 1200px;
  }
  .title { position: absolute; inset: 0; font-weight: normal; }
  .label-box {
    position: absolute;
    background: var(--paper);
    color: var(--ink);
    font-family: "Graduate", sans-serif;
    display: flex; align-items: center; justify-content: center;
    clip-path: polygon(0 6%, 100% 0, 98% 100%, 2% 94%);
  }
  .label-the   { left: 287px; top: 253px; width: 193px; height: 44px; font-size: 44px; letter-spacing: 4px; }
  .label-of    { left: 304px; top: 533px; width: 156px; height: 40px; font-size: 36px; letter-spacing: 3px; }
  .ribbon {
    position: absolute;
    background: var(--ribbon);
    display: flex; align-items: center; justify-content: center;
    clip-path: polygon(0 0, 100% 4%, 96% 50%, 100% 100%, 0 96%, 4% 50%);
  }
  .ribbon-honest {
    left: 50px; top: 304px; width: 681px; height: 96px;
    font-family: "Graduate", sans-serif; font-size: 92px; letter-spacing: 12px;
  }
  .ribbon-chaos {
    left: 133px; top: 400px; width: 514px; height: 88px;
    font-family: "Graduate", sans-serif; font-size: 88px; letter-spacing: 10px;
  }
  .ribbon-the {
    left: 83px; top: 540px; width: 97px; height: 44px;
    transform: rotate(-4deg);
    font-family: "Graduate", sans-serif; font-size: 30px; color: var(--ink);
  }
  .ribbon-last {
    left: 40px; top: 592px; width: 700px; height: 126px;
    transform: rotate(-4deg);
    font-family: "Permanent Marker", sans-serif; font-size: 120px; letter-spacing: 4px;
    text-shadow: 5px 5px 0 var(--ribbon-deep);
  }
  .ribbon-last span { display: block; transform: translateY(14px); }
  .ribbon-little {
    left: 360px; top: 742px; width: 240px; height: 80px;
    transform: rotate(-5deg);
    font-family: "Permanent Marker", sans-serif; font-size: 34px;
    text-shadow: 3px 3px 0 var(--ribbon-deep);
  }
  .byline {
    position: absolute;
    left: 52px; right: 40px; top: 1124px;
    display: flex; align-items: baseline; gap: 26px;
    white-space: nowrap;
  }
  .byline-by { color: var(--ribbon); font-weight: 700; font-size: 22px; letter-spacing: 4px; }
  .byline-name {
    font-weight: 600; font-size: 37px; letter-spacing: 7px;
    text-transform: uppercase;
  }
</style>
</head>
<body>
<main class="cover">
  <p class="kicker">FROM THE POPULAR BLOG</p>

  <svg class="tree-art" role="img" aria-label="Illustration of a bare white winter tree with a tall trunk and spreading branches filling the cover" viewBox="0 0 776 1200">
    <defs>
      <radialGradient id="crown-glow" cx="50%" cy="50%" r="50%">
        <stop offset="0%" stop-color="var(--branch-light)" stop-opacity="0.85"/>
        <stop offset="60%" stop-color="var(--branch-mid)" stop-opacity="0.6"/>
        <stop offset="100%" stop-color="var(--ink)" stop-opacity="0"/>
      </radialGradient>
      <linearGradient id="trunk-fade" x1="0" y1="0" x2="0" y2="1">
        <stop offset="0%" stop-color="var(--trunk)" stop-opacity="0.4"/>
        <stop offset="100%" stop-color="var(--trunk)" stop-opacity="1"/>
      </linearGradient>
    </defs>
    <ellipse cx="388" cy="460" rx="390" ry="470" fill="url(#crown-glow)"/>
    <path d="M268 700 L292 700 L300 1150 L262 1150 Z" fill="url(#trunk-fade)"/>
    <ellipse cx="282" cy="1158" rx="70" ry="8" fill="var(--trunk)" opacity="0.8"/>
  </svg>

  <h1 class="title" aria-label="The Honest Chaos Of The Last Little One">
    <span class="label-box label-the">THE</span>
    <span class="ribbon ribbon-honest">HONEST</span>
    <span class="ribbon ribbon-chaos">CHAOS</span>
    <span class="label-box label-of">OF</span>
    <span class="ribbon ribbon-the">THE</span>
    <span class="ribbon ribbon-last"><span>LAST</span></span>
    <span class="ribbon ribbon-little">LITTLE ONE</span>
  </h1>

  <p class="byline">
    <span class="byline-by">BY</span>
    <span class="byline-name">Loretta Vanstrand</span>
  </p>
</main>
</body>
</html>
```